Letter Head Design

I need a letter head design based on my company logo that I attached.
Include phone number: (403)582-4316
Address: 347 14th Avenue NE, Calgary, Alberta, Canada, T3K 4R8

Industry/Entity Type

It Company

```html
<!DOCTYPE html>
<html lang="en">
<head>
<meta charset="utf-8">
<title>HavenRoom Interiors Corp. – Letterhead</title>
<link rel="stylesheet" href="https://fonts.googleapis.com/css2?family=Source+Sans+3:wght@400;600&display=swap">
<style>
  :root {
    --backdrop: #e6e6e4;
    --paper: #ffffff;
    --paper-edge: #2b2b2b;
    --brand-blue: #1f64ae;
    --brand-green: #4fae3f;
    --ink: #4a4a4a;
    --rule: #9a9a9a;
    --mark-faint: #e9eef5;
  }
  html, body {
    margin: 0;
    padding: 0;
    width: 952px;
    height: 1200px;
    overflow: hidden;
    background: var(--backdrop);
  }
  .canvas {
    position: relative;
    width: 952px;
    height: 1200px;
  }
  .letterhead {
    position: absolute;
    left: 58px;
    top: 58px;
    width: 835px;
    height: 1082px;
    background: var(--paper);
    border: 1px solid var(--paper-edge);
    box-sizing: border-box;
    font-family: "Source Sans 3", "Myriad Pro", Arial, sans-serif;
  }
  .brand {
    position: absolute;
    left: 38px;
    top: 120px;
    display: flex;
    align-items: center;
    gap: 10px;
  }
  .brand-square {
    width: 22px;
    height: 22px;
    background: var(--brand-green);
    border-radius: 3px;
  }
  .brand-name {
    font-size: 23px;
    font-weight: 600;
    color: var(--brand-blue);
    letter-spacing: -0.2px;
    line-height: 1;
  }
  .contact {
    position: absolute;
    left: 608px;
    top: 62px;
    padding-left: 9px;
    border-left: 1px solid var(--rule);
    color: var(--ink);
    font-size: 13px;
    line-height: 16px;
  }
  .contact-phone {
    display: flex;
    align-items: center;
    gap: 4px;
    margin: 0 0 10px;
  }
  .contact-phone svg {
    width: 9px;
    height: 9px;
  }
  .contact-address {
    margin: 0;
    font-style: normal;
  }
  .backdrop-mark {
    position: absolute;
    left: 210px;
    top: 424px;
    width: 415px;
    height: 414px;
  }
</style>
</head>
<body>
  <div class="canvas">
    <div class="letterhead">
      <div class="brand">
        <span class="brand-square" aria-hidden="true"></span>
        <span class="brand-name">HavenRoom Interiors Corp.</span>
      </div>

      <div class="contact">
        <p class="contact-phone">
          <svg viewBox="0 0 10 10" aria-hidden="true">
            <path d="M2.2 0.8 L3.6 2.6 L2.8 3.6 Q3.8 5.8 6.2 7 L7.2 6.2 L9.2 7.6 L8.2 9.2 Q4.2 9 0.8 2 Z" fill="none" stroke="#4a4a4a" stroke-width="0.9" stroke-linejoin="round"/>
          </svg>
          (403)582-4316
        </p>
        <address class="contact-address">
          347 14th Avenue NE<br>
          Calgary, Alberta, Canada, T3K 4R8
        </address>
      </div>

      <svg class="backdrop-mark" viewBox="0 0 415 414" aria-hidden="true">
        <rect x="9" y="9" width="397" height="396" rx="20" fill="none" stroke="var(--mark-faint)" stroke-width="18"/>
      </svg>
    </div>
  </div>
</body>
</html>
```